Corporate charity needs interactive web page

Harbourline Mutual Foundation has commissioned a research organisation to develop a "vision" for financial inclusion (enabling low income people to access free financial advice, banking, affordable credit, etc). The aim is to create a coherent vision to unite disparate service providers, charities, associations, policy-makers and individuals under a common set of goals.

We have that "vision" document, but we want to:
1) break up the text from a report into a series of pages, putting some of the more detailed sections into boxes that appear if one hovers over it;
2) enable the audience to comment on it in a visual way - what's missing, provide examples of things discussed, add general comments - that is visible to others, trackable and moderated. Like posting post-it notes on flip charts. Users should be able to navigate to and from the pages.
3) We also would like to be able to collate responses in a textual form;
4) Have a stand alone identity but with the facility to link to it and create links to other pages on other sites.
Updates

Target Market(s)

Charities and others working on finanical inclusion activities/ policy in the UK

Industry/Entity Type

Financial

Requirements
Must have
• 1) break up the text from a report into a series of pages, putting some of the more detailed sections into boxes that appear if one hovers over it;
2) enable the audience to comment on it in a visual way that is visible to others, trackable and moderated. Users should be able to navigate to and from the pages.
3) able to collate responses in a textual form;
4) a stand alone identity but with the facility to link to it and create links to other pages on other sites.
Nice to have
• Attached are our corporate branding guidelines, however we do not require any slavish adherence to them as the site will be stand alone, with links to our site and others.

```html
<!DOCTYPE html>
<html lang="en">
<head>
<meta charset="utf-8">
<title>Report from Projects – Harbourline Mutual Foundation</title>
<link rel="stylesheet" href="https://fonts.googleapis.com/css2?family=Cinzel:wght@600;700&family=Open+Sans:ital,wght@0,400;0,600;0,700;1,400&display=swap">
<style>
:root{
  --page-bg:#f5f6fc;
  --canvas-bg:#f4f4f4;
  --frame:#c9c9cf;
  --brand-blue:#0c4a85;
  --brand-light:#2a9fd6;
  --intro-bg:#e5e7ee;
  --intro-text:#1d5a9a;
  --red-top:#b3343f;
  --red-bottom:#5c0a13;
  --text:#2b2b2b;
  --muted:#555;
  --footer:#004a80;
  --tip-bg:#fbfbe6;
}
*{box-sizing:border-box;margin:0;padding:0}
html,body{width:1037px;height:1200px;overflow:hidden;background:var(--canvas-bg)}
body{font-family:"Open Sans",Arial,sans-serif;color:var(--text)}
.stage{position:absolute;left:0;top:0;width:1200px;height:1389px;transform:scale(.86417);transform-origin:0 0}
.page{position:absolute;left:120px;top:0;width:960px;height:1350px;background:var(--page-bg);border:1px solid var(--frame);border-top:none}
.abs{position:absolute}
.caps{font-family:"Cinzel",Georgia,serif;font-weight:700}

/* header */
.brand{left:20px;top:20px;display:flex;align-items:center;gap:12px}
.brand-square{width:46px;height:46px;background:var(--brand-blue)}
.brand-name{font-size:16px;font-weight:700;line-height:20px;color:var(--brand-blue);width:140px}
.site-title{left:260px;top:22px;width:440px;text-align:center;font-size:26px;line-height:34px;color:#3a3a3a;font-weight:600;letter-spacing:.5px;white-space:nowrap}
.title-rule{left:340px;top:63px;width:280px;height:3px;background:#222;border-radius:2px}

/* hero */
.hero-photo{left:0;top:100px;width:500px;height:300px;background:linear-gradient(120deg,#7d8b5a 0%,#a88a70 35%,#c9c2b0 60%,#6b6f5a 100%)}
.search{left:500px;top:100px;width:460px;height:300px;background:linear-gradient(180deg,var(--red-top),var(--red-bottom))}
.search h2{position:absolute;left:80px;top:32px;width:300px;text-align:center;color:#fff;font-size:21px;padding-bottom:4px;border-bottom:2px solid #f1dadd;white-space:nowrap}
.field-label{position:absolute;width:130px;text-align:right;color:#fff;font-size:17px;left:0}
.field{position:absolute;height:25px;background:#fff;border:2px solid #d9b3b7;border-radius:2px}
.select-arrow{position:absolute;right:2px;top:2px;width:17px;height:17px;background:#9c1f2a;border-radius:2px}
.select-arrow svg{display:block}
.submit{position:absolute;left:150px;top:200px;width:150px;height:30px;border-radius:4px;background:linear-gradient(180deg,#f2545c,#c41f2a);border:1px solid #e98f94;color:#fff;font-size:14px;text-align:center;line-height:28px}

/* intro */
.intro{left:0;top:400px;width:960px;height:130px;background:var(--intro-bg);padding:16px 20px;color:var(--intro-text);font-size:12.5px;line-height:17px}
.intro p+p{margin-top:16px;font-style:italic}

/* article list */
.list{left:0;top:530px;width:310px;height:670px;border-right:1px solid #dedee6}
.list-head{height:30px;background:var(--brand-blue);color:#fff;font-size:12.5px;line-height:30px;padding-left:20px;position:relative}
.list-nav{position:absolute;right:10px;top:9px}
.list-item{height:70px;padding:7px 12px 0 20px;font-size:12.5px;line-height:17px;color:#222;border-bottom:1px solid #e8e8ee;background:linear-gradient(180deg,#f5f6fc 70%,#ecedf3)}
.list-item.is-active{background:#ebebef;position:relative}
.active-pointer{position:absolute;right:-20px;top:0}

/* article */
.article{left:340px;top:546px;width:600px}
.article h1{font-size:16.5px;font-weight:400;color:var(--brand-light);line-height:22px}
.article p{font-size:12.5px;line-height:17px;margin-top:14px}
.article .author{color:var(--brand-light)}
.btn{display:inline-block;background:linear-gradient(180deg,#3bb0e6,#1a87c3);color:#fff;font-size:12.5px;border:1px solid #0e6aa0;border-radius:2px;box-shadow:0 1px 2px rgba(0,0,0,.3)}
.read-more{left:340px;top:770px;width:101px;height:21px;line-height:19px;text-align:center}
.comments{left:311px;top:810px;width:649px;height:390px;background:#f1f2f9}
.comments .label{position:absolute;left:29px;font-size:14px;color:var(--muted)}
.comment-text{position:absolute;left:29px;top:36px;width:580px;font-size:12.5px;line-height:17px}
.input{position:absolute;left:29px;width:201px;height:21px;background:#fff;border:1px solid #9aa}
.input-label{position:absolute;left:240px;font-size:14px;color:var(--muted)}
.textarea{position:absolute;left:29px;top:209px;width:541px;height:101px;background:#fff;border:1px solid #9aa}
.post{position:absolute;left:29px;top:320px;width:101px;height:21px;line-height:19px;text-align:center}

/* tooltip */
.tooltip{left:530px;top:590px;width:230px;height:70px;background:var(--tip-bg);border:1px solid #c6c6b4;box-shadow:0 1px 4px rgba(0,0,0,.2);font-size:12.5px;line-height:17px;color:#333}
.tooltip-photo{position:absolute;left:9px;top:8px;width:53px;height:53px;background:linear-gradient(160deg,#6b4a38,#c69a80)}
.tooltip-text{position:absolute;left:70px;top:7px;width:150px}
.tooltip-tail{position:absolute;left:18px;bottom:-11px}

/* footer */
.footer{left:0;top:1200px;width:960px;height:110px;background:var(--footer);box-shadow:inset 0 6px 8px rgba(0,0,0,.35);text-align:center;padding-top:30px}
.footer nav{color:#fff;font-size:17px;line-height:22px;white-space:nowrap}
.footer a{color:#fff;text-decoration:none;margin:0 13px}
.copyright{left:0;top:1322px;width:960px;text-align:center;font-size:12px;color:#555;letter-spacing:.3px}
</style>
</head>
<body>
<div class="stage">
<div class="page">

  <header>
    <div class="abs brand">
      <span class="brand-square"></span>
      <span class="brand-name">Harbourline Mutual Foundation</span>
    </div>
    <div class="abs site-title caps">Report from Projects</div>
    <div class="abs title-rule"></div>
  </header>

  <div class="abs hero-photo" role="img" aria-label="Photo of an older couple smiling at a laptop"></div>

  <section class="abs search">
    <h2 class="caps">Search Report</h2>
    <span class="field-label caps" style="top:80px">Title</span>
    <span class="field" style="left:150px;top:80px;width:200px"></span>
    <span class="field-label caps" style="top:120px">Type</span>
    <span class="field" style="left:150px;top:120px;width:200px">
      <span class="select-arrow"><svg width="17" height="17"><path d="M5 7h7l-3.5 4z" fill="#fff"/></svg></span>
    </span>
    <span class="field-label caps" style="top:160px">Period</span>
    <span class="field" style="left:150px;top:160px;width:120px">
      <span class="select-arrow"><svg width="17" height="17"><path d="M5 7h7l-3.5 4z" fill="#fff"/></svg></span>
    </span>
    <span class="field" style="left:280px;top:160px;width:70px">
      <span class="select-arrow"><svg width="17" height="17"><path d="M5 7h7l-3.5 4z" fill="#fff"/></svg></span>
    </span>
    <span class="submit caps">Submit</span>
  </section>

  <section class="abs intro">
    <p>This is a complete listing of all the reports published with the Foundation’s support, starting with the most recent. To be more selective, use the facilities on the right to search by report type or to list all reports for a particular month or year. Please press 'Reset' between multiple searches.</p>
    <p>You may download, store and use these for your own personal use and research, or that of your charity, company or organisation. If you wish to republish, retransmit, redistribute or make them available to another party, please seek our prior consent. Please also note that the views expressed are those of the authors and not necessarily those of the Foundation</p>
  </section>

  <aside class="abs list">
    <div class="list-head">Showing 1 - 5 of 200 articles
      <svg class="list-nav" width="24" height="12"><path d="M9 0v12L1 6z" fill="#8fb0d4"/><path d="M15 0v12l8-6z" fill="#fff"/></svg>
    </div>
    <div class="list-item is-active">Credit and low-income consumers: a demand-side perspective on the issues for consumer protection »
      <svg class="active-pointer" width="21" height="70"><path d="M0 0L20 35L0 70" fill="#ebebef" stroke="#d4d4dc"/></svg>
    </div>
    <div class="list-item">Can consumer credit be affordable to house-holds on low incomes ? »</div>
    <div class="list-item">Overcoming the barriers to long-term thinking in financial markets »</div>
    <div class="list-item">The way we pay: payment systems and financial inclusion »</div>
    <div class="list-item">The development of a performance framework for community development finance institu-tions (Change Matters) »</div>
  </aside>

  <article class="abs article">
    <h1>Credit and low-income consumers: a demand-side perspective on the issues for consumer protection</h1>
    <p>This study explores the benefits, risks and outcomes of credit use by low-income con-sumers, who are among the most exposed, to provide a robust evidence base to feed into current policy and regulatory debate.</p>
    <p>This study was carried out by <span class="author">Nora Halden</span>, Tom Brenner and Jane Corwell for Veritas Insight and Mark D. Ashby of Northgate City University. It aims to bring a consumer perspective and an understanding of the dynamics of the types of credit people want and need to the public and regulatory debate. It seeks to provide a robust evidence base about how people on low incomes use credit, why they choose the credit they use and the problems they face with the credit available to them.</p>
  </article>
  <span class="abs btn read-more">Read more...</span>

  <section class="abs comments">
    <span class="label" style="top:16px">Comment</span>
    <p class="comment-text"><b>Lorem ipsum,</b> dolor sit amet, consectetur adipisicing elit, sed do eiusmod tempor incididunt ut labore et dolore magna aliqua. Ut enim ad minim veniam, quis nostrud exercitation ullamco laboris nisi ut aliquip ex ea commodo consequat. Duis aute irure dolor in reprehenderit in voluptate velit esse cillum dolore eu fugiat nulla pariatur.</p>
    <span class="label" style="top:126px">Leave a comment</span>
    <span class="input" style="top:149px"></span><span class="input-label" style="top:150px">Your Name</span>
    <span class="input" style="top:179px"></span><span class="input-label" style="top:180px">Your Email</span>
    <span class="textarea"></span>
    <span class="btn post">Post comment</span>
  </section>

  <div class="abs tooltip">
    <div class="tooltip-photo" role="img" aria-label="Portrait of the study author"></div>
    <div class="tooltip-text">Nora Halden, teacher of Northgate City University</div>
    <svg class="tooltip-tail" width="22" height="11"><path d="M0 0L11 10L22 0" fill="#fbfbe6" stroke="#c6c6b4"/><path d="M1 0h20" stroke="#fbfbe6" stroke-width="2"/></svg>
  </div>

  <footer class="abs footer">
    <nav class="caps">
      <a>Home</a><a>About us</a><a>Our people</a><a>News</a><a>Projects</a><a>Reports</a><br>
      <a>Our giving programme</a><a>Downloadable resource</a>
    </nav>
  </footer>
  <div class="abs copyright">Copyright 2012 by Harbourline Mutual Foundation</div>

</div>
</div>
</body>
</html>
```